Cat-products company needs smart, yet endearing, business card

We need a business card design for a new, but up-and-running, business based in Honolulu, Hawaii. The business is Purrlane Nest Co. Our first product is the most environmentally-friendly cat grass kit ever seen on the planet. Future products, currently in the R&D phase, will include a variety of exciting cat scratchers. We also do consulting work to help apartment-dwellers make their home more cat-friendly and, in the future, plan on doing full, custom installs of structure to create high walkways for cats.

Target Market(s)

Middle-aged, apartment-dwelling, middle-class workers who own 1 or more cats and who dote on them.

Industry/Entity Type

Pet Care

Contact Information for Business Card

A striking, professional, yet warm and friendly design is what we're after.

Font styles to use
Serif
Sans Serif
Other font styles liked:
• Comfortaa

Colors

Designer to choose colors to be used in the design.

Requirements
Must have
• The company logo: (see attachment)
• The company name: Purrlane Nest Co
• The web address: www.purrlanenestco.example
• Email: support@purrlanenestco.example
• Phone: +1 (808) 555 0172
• Update (Fri Jun 30 3017 7:45pm Hawaii Time) I would like, is possible, uploaded picture of the cat grass kit on the back of the card with some text along the lines of: Purrlane Nest Co - Where The Freshest Kitty Sprouts Begin
Nice to have
• A cat picture, cartoon, real or silhouette that illustrates cats in action and/or relaxing; ie using the apartment space to live, play and relax in and being well-contented.
• Most of the website is done in the font: Comfortaa. It might be nice to continue using this for brand consistency.
Should not have
• Hard-to-read fonts.

```html
<!DOCTYPE html>
<html lang="en">
<head>
<meta charset="utf-8">
<title>Purrlane Nest Co – Business Card</title>
<link rel="stylesheet" href="https://fonts.googleapis.com/css2?family=Comfortaa:wght@400;700&family=Dosis:wght@600;700&display=swap">
<style>
  :root {
    --brown: #5e3530;
    --brown-dark: #4a2925;
    --yellow: #e8b21a;
    --paper: #ffffff;
    --paper-shade: #ececec;
    --backdrop: #e9e5df;
    --photo-warm-1: #e9d8c3;
    --photo-warm-2: #c9a584;
    --photo-cool-1: #eef0f1;
    --photo-cool-2: #cfc7bd;
  }
  * { box-sizing: border-box; margin: 0; padding: 0; }
  html, body { width: 1200px; height: 780px; overflow: hidden; }
  body {
    background: var(--backdrop);
    position: relative;
    font-family: "Comfortaa", sans-serif;
  }
  .card {
    position: absolute;
    width: 540px;
    height: 310px;
    box-shadow: 0 10px 24px rgba(60, 40, 30, 0.25);
    overflow: hidden;
  }

  /* Front */
  .card-front { left: 36px; top: 235px; background: var(--paper); }
  .front-header {
    position: absolute; left: 0; top: 0; width: 100%; height: 130px;
    background: linear-gradient(180deg, #fafafa, var(--paper-shade));
  }
  .brand-name {
    position: absolute; left: 28px; top: 46px;
    font-family: "Dosis", sans-serif; font-weight: 700;
    font-size: 40px; line-height: 1; color: var(--yellow);
    letter-spacing: 0.5px; text-transform: uppercase;
    width: 230px;
  }
  .contact {
    position: absolute; left: 290px; top: 34px;
  }
  .employee-name {
    font-family: "Dosis", sans-serif; font-weight: 600;
    font-size: 22px; color: var(--brown); letter-spacing: 0.5px;
    margin-bottom: 12px;
  }
  .contact-line {
    display: flex; align-items: center; gap: 7px;
    font-size: 11px; color: var(--brown); margin-bottom: 5px;
  }
  .contact-line svg { width: 14px; height: 14px; flex: none; }
  .rule-yellow {
    position: absolute; left: 0; top: 136px; width: 100%; height: 4px;
    background: var(--yellow);
  }
  .photo-strip {
    position: absolute; left: 0; top: 146px; width: 100%; height: 98px;
    display: flex; gap: 3px; background: var(--paper);
  }
  .photo { flex: 1; }
  .photo-1 { background: linear-gradient(135deg, var(--photo-warm-1), var(--photo-warm-2)); }
  .photo-2 { background: linear-gradient(135deg, var(--photo-cool-1), var(--photo-cool-2)); }
  .photo-3 { background: linear-gradient(135deg, #f1ede8, #b9a58e); }
  .photo-4 { background: linear-gradient(135deg, #f3f1ee, #a98a6c); }
  .front-band {
    position: absolute; left: 0; top: 250px; width: 100%; height: 60px;
    background: var(--brown);
    border-top: 3px solid var(--paper);
    display: flex; align-items: center; justify-content: flex-end;
    padding-right: 26px;
  }
  .web {
    color: var(--yellow); font-size: 14px; font-weight: 700; letter-spacing: 2px;
  }

  /* Back */
  .card-back {
    left: 624px; top: 235px;
    background: var(--brown);
    padding: 11px;
  }
  .back-inner {
    width: 100%; height: 100%;
    background: radial-gradient(circle at 50% 45%, #ffffff, #e4e4e4);
    display: flex; flex-direction: column; align-items: center; justify-content: center;
    gap: 16px;
  }
  .back-brand {
    display: flex; align-items: center; gap: 12px;
  }
  .brand-mark {
    width: 34px; height: 34px; background: var(--brown);
  }
  .back-brand .brand-label {
    font-family: "Dosis", sans-serif; font-weight: 700;
    font-size: 36px; color: var(--yellow); text-transform: uppercase;
    letter-spacing: 0.5px;
  }
  .back-web {
    color: var(--yellow); font-size: 12px; font-weight: 700; letter-spacing: 2px;
  }
</style>
</head>
<body>
  <section class="card card-front">
    <div class="front-header">
      <div class="brand-name">Purrlane Nest Co</div>
      <div class="contact">
        <div class="employee-name">EMPLOYEE NAME</div>
        <div class="contact-line">
          <svg viewBox="0 0 14 14" aria-hidden="true"><circle cx="7" cy="7" r="6.5" fill="none" stroke="#e8b21a"/><path d="M4.5 4h1.6l.6 1.6-.9.7a5 5 0 0 0 2 2l.7-.9 1.6.6V9.6c0 .4-.4.8-.9.7A6 6 0 0 1 3.8 4.9c-.1-.5.3-.9.7-.9z" fill="#e8b21a"/></svg>
          <span>+1 (808) 555 0172</span>
        </div>
        <div class="contact-line">
          <svg viewBox="0 0 14 14" aria-hidden="true"><circle cx="7" cy="7" r="6.5" fill="none" stroke="#e8b21a"/><rect x="3.8" y="4.8" width="6.4" height="4.6" fill="none" stroke="#e8b21a" stroke-width="0.9"/><path d="M3.8 4.8 7 7.4l3.2-2.6" fill="none" stroke="#e8b21a" stroke-width="0.9"/></svg>
          <span>support@purrlanenestco.example</span>
        </div>
      </div>
    </div>
    <div class="rule-yellow"></div>
    <div class="photo-strip">
      <div class="photo photo-1" role="img" aria-label="Photo of a kitten playing with a toy"></div>
      <div class="photo photo-2" role="img" aria-label="Photo of a white kitten chewing a toy mouse"></div>
      <div class="photo photo-3" role="img" aria-label="Photo of a tabby kitten lying down"></div>
      <div class="photo photo-4" role="img" aria-label="Photo of a row of kittens"></div>
    </div>
    <div class="front-band">
      <span class="web">www.purrlanenestco.example</span>
    </div>
  </section>

  <section class="card card-back">
    <div class="back-inner">
      <div class="back-brand">
        <span class="brand-label">Purrlane Nest Co</span>
        <span class="brand-mark" aria-hidden="true"></span>
      </div>
      <div class="back-web">www.purrlanenestco.example</div>
    </div>
  </section>
</body>
</html>
```